PowerPoint Design Project

I need a Power Point slide template designed with 4 or 5 slides. We are a health care technology company and would like to take our current look and feel in this PP presentation to the next level and "prettied up"

Target Market(s)

Health Care Professionals

Industry/Entity Type

Health

Requirements
Must have
• Cannot change out the TOLVARE logo. The logo is all CAPS
Should not have
• The color blue is restricted and cannot be used.

```html
<!DOCTYPE html>
<html lang="en">
<head>
<meta charset="utf-8">
<title>Tolvare Slide Template</title>
<link href="https://fonts.googleapis.com/css2?family=Open+Sans:wght@400;600;700&family=Questrial&display=swap" rel="stylesheet">
<style>
  :root {
    --stage: #ebe7e1;
    --slide: #f3f3f5;
    --green: #a3b631;
    --grey-logo: #9a9a9a;
    --grey-text: #5a5a5a;
    --grey-dark: #555555;
    --rule: #9b9b9b;
    --white: #ffffff;
  }
  * { margin: 0; padding: 0; box-sizing: border-box; }
  html, body { width: 1200px; height: 632px; overflow: hidden; background: var(--stage); }
  .stage { position: relative; width: 1200px; height: 632px; }

  .slide {
    position: absolute; width: 358px; height: 268px;
    background: var(--slide);
    box-shadow: 0 1px 3px rgba(0,0,0,0.15);
    overflow: hidden;
  }
  .slide--cover { left: 34px; top: 26px; }
  .slide--intro { left: 416px; top: 26px; }
  .slide--wide-photo { left: 794px; top: 26px; }
  .slide--team { left: 33px; top: 315px; }
  .slide--split { left: 419px; top: 315px; }
  .slide--closing { left: 793px; top: 315px; }

  .header-bar {
    position: absolute; left: 12px; top: 11px; width: 333px; height: 28px;
    background: var(--green);
    border-radius: 12px 0 12px 0;
    color: var(--white);
    font: 700 15px/28px "Open Sans", sans-serif;
    text-align: center; letter-spacing: 0.2px;
  }

  .body-copy {
    position: absolute;
    font: 400 8.4px/10.6px "Questrial", sans-serif;
    color: var(--grey-text);
    text-align: justify;
  }

  .bullet-list { position: absolute; left: 30px; top: 140px; list-style: none; }
  .bullet-list li {
    position: relative; padding-left: 12px; height: 16px;
    font: 600 8.4px/16px "Open Sans", sans-serif; color: var(--grey-dark);
  }
  .bullet-list li::before {
    content: ""; position: absolute; left: 0; top: 6px;
    width: 4px; height: 4px; background: var(--green);
  }

  .photo { position: absolute; }

  .brand {
    position: absolute; display: flex; align-items: center; gap: 12px;
  }
  .brand-mark { width: 26px; height: 26px; background: var(--green); }
  .brand-name {
    font: 700 30px/1 "Open Sans", sans-serif; color: var(--grey-logo);
    letter-spacing: 3px;
  }

  .title-pill {
    position: absolute; left: 13px; top: 169px; width: 333px; height: 46px;
    background: var(--green); border-radius: 12px 0 12px 12px;
    color: var(--white); font: 700 15px/46px "Open Sans", sans-serif;
    text-align: center;
  }

  .thanks {
    position: absolute; left: 0; width: 358px; text-align: center; color: var(--grey-dark);
  }
  .thanks--big { top: 140px; font: 400 25px/1 "Questrial", sans-serif; }
  .thanks--small { top: 176px; font: 700 14px/1 "Open Sans", sans-serif; letter-spacing: 0.5px; }

  .footer-url {
    position: absolute; right: 12px; bottom: 6px;
    border-left: 1px solid var(--rule); padding-left: 5px; height: 16px;
    font: 400 8.6px/20px "Questrial", sans-serif; color: var(--grey-dark);
  }
  .footer-url span { color: var(--green); }
</style>
</head>
<body>
<main class="stage">

  <section class="slide slide--cover">
    <div class="brand" style="left:68px; top:102px;">
      <div class="brand-mark"></div>
      <div class="brand-name">TOLVARE</div>
    </div>
    <div class="title-pill">TITLE OF PRESENTATION</div>
    <div class="footer-url">www.<span>tolvarehealth</span>.com</div>
  </section>

  <section class="slide slide--intro">
    <div class="header-bar">INTRODUCTION SLIDE</div>
    <p class="body-copy" style="left:30px; top:37px; width:300px;">Orem ipsum d olor sit amet, consectetuer adipiscing elit, sed diam nonummy nibh euismod tincidunt ut laoreet dolore magna aliquam erat volutpat. Ut wisi enim ad minim veniam, quis nostrud exerci tation ullamcoper suscipit lobortis nisl ut aliquip ex ea commodo consequat. Duis autem vel eum iriure dolor in hendrerit in vulputate velit esse molestie consequat, vel illum dolore eu feugiat nulla facilisis.</p>
    <ul class="bullet-list">
      <li>Lorem ipsum &nbsp;Lorem Lorem ipsum &nbsp;Lorem</li>
      <li>Lorem ipsum Lorem Lorem</li>
      <li>Lorem ipsum Lorem Lorem ipsum &nbsp;Lorem &nbsp;Lorem ipsum</li>
      <li>Lorem ipsum orem Lorem ipsum &nbsp;Lo</li>
      <li>Lorem ipsum Lorem</li>
    </ul>
    <div class="footer-url">www.<span>tolvarehealth</span>.com</div>
  </section>

  <section class="slide slide--wide-photo">
    <div class="header-bar">LOREM IPSUMLOREM IPSUM</div>
    <p class="body-copy" style="left:21px; top:39px; width:300px;">Lorem ipsum d olor sit amet, consectetuer adipiscing elit, sed diam nonummy nibh euismod tincidunt ut laoreet dolore magna aliquam erat volutpat. Ut wisi enim ad minim veniam, quis nostrud exerci tation ullamcoper suscipit lobortis nisl ut</p>
    <div class="photo" role="img" aria-label="Photo of a stethoscope resting on medical paperwork"
         style="left:12px; top:103px; width:333px; height:138px; background:linear-gradient(120deg,#eef1f4 0%,#c9d0d8 45%,#7d8791 70%,#d9dde2 100%);"></div>
    <div class="footer-url">www.<span>tolvarehealth</span>.com</div>
  </section>

  <section class="slide slide--team">
    <div class="header-bar">LOREM IPSUMLOREM IPSUM</div>
    <p class="body-copy" style="left:18px; top:45px; width:300px;">Orem ipsum d olor sit amet, consectetuer adipiscing elit, sed diam nonummy nibh euismod tincidunt ut laoreet dolore magna aliquam erat volutpat. Ut wisi enim ad minim veniam, quis nostrud exerci tation ullamcoper suscipit lobortis nisl ut.</p>
    <div class="photo" role="img" aria-label="Photo of a smiling doctor seated at a desk in a bright office"
         style="left:15px; top:97px; width:327px; height:143px; background:linear-gradient(90deg,#e4e7ea 0%,#d8d5d2 35%,#eef0f2 65%,#5a5d61 100%);"></div>
    <div class="footer-url">www.<span>tolvarehealth</span>.com</div>
  </section>

  <section class="slide slide--split">
    <div class="header-bar">LOREM IPSUMLOREM IPSUM</div>
    <p class="body-copy" style="left:21px; top:55px; width:127px;">Lorem ipsum d olor sit amet, consectetuer adipiscing elit, sed diam nonummy nibh euismod tincidunt ut laoreet dolore magna aliquam erat volutpat. Ut wisi enim ad minim veniam, quis nostrud exerci tation ullamcoper suscipit lobortis nisl ut aliquip ex ea commodo consequat. Duis autem vel eum iriure.<br>Ut wisi enim ad minim veniam, quis nostrud exerci tation ullamcoper suscipit lobortis nisl ut aliquip ex ea commodo consequat. Duis autem vel eum iriure.</p>
    <div class="photo" role="img" aria-label="Photo of a doctor holding a stethoscope toward the viewer"
         style="left:161px; top:56px; width:185px; height:181px; background:linear-gradient(135deg,#dfe7ec 0%,#eef1f3 40%,#d7c7bb 60%,#e9edf0 100%);"></div>
    <div class="footer-url">www.<span>tolvarehealth</span>.com</div>
  </section>

  <section class="slide slide--closing">
    <div class="brand" style="left:68px; top:86px;">
      <div class="brand-mark"></div>
      <div class="brand-name">TOLVARE</div>
    </div>
    <div class="thanks thanks--big">THANK YOU!</div>
    <div class="thanks thanks--small">FOR YOUR ATTENTION</div>
    <div class="footer-url">www.<span>tolvarehealth</span>.com</div>
  </section>

</main>
</body>
</html>
```